yieldcompassplans.com needs a good website design and logo

Our company sells memberships to a website that generates systematic rules-based investment strategies on a monthly basis.
I would like a modern professional wordpress design that uses the color blue. It should communicate financial safety and growth. The company is based in Denver Colorado USA.
Please see current website: https://www.yieldcompassplans.com

Target Market(s)

individual investors looking to improve their investment performance. Looking for improved returns or ways to limit losses.

Industry/Entity Type

Investment

Logo Text

yieldcompassPlans

Coding

Coded - Design and coding required

Font styles to use
Sans Serif

Colors
3176b5
85abd2
0355a3
00a990

Requirements
Must have
• I've included details in the attached document.
• The colors selected below are suggestions. While we want the color blue, please use the best version of blue you think is good.
Nice to have
• The design with work with wordpress. We would like to be able to modify the theme later using elementor and a base theme, like maybe astra?
• There is additional work to be done after this contest including designing other pages.
• The site uses some plotvanery.com to display charts and investment performance, if you have experience making these charts and graphs look good, that would be valuable.

```html
<!DOCTYPE html>
<html lang="en">
<head>
<meta charset="utf-8">
<title>yieldcompassPlans</title>
<link rel="stylesheet" href="https://fonts.googleapis.com/css2?family=Oswald:wght@400;500&family=Mulish:ital,wght@0,400;0,600;0,700;1,400&display=swap">
<style>
:root{
  --green:#7dc243;
  --green-dark:#5fa52c;
  --navy:#1c3868;
  --navy-deep:#13284d;
  --ink:#1f2d44;
  --text:#3a4454;
  --muted:#6d7684;
  --light:#f0f0f0;
  --line:#dfe3e8;
  --white:#ffffff;
  --footer:#1f1f1f;
}
*{box-sizing:border-box;margin:0;padding:0}
html,body{width:1200px;height:4255px;overflow:hidden}
body{font-family:"Mulish",sans-serif;color:var(--text);background:var(--white);position:relative}
.abs{position:absolute}
h2.section-title{font-family:"Oswald",sans-serif;font-weight:400;font-size:34px;color:var(--ink);text-align:center;position:absolute;left:0;width:1200px}
h2.section-title span{color:var(--green)}
.btn{display:inline-flex;align-items:center;height:34px;font-size:13px;font-weight:700;color:var(--ink);text-decoration:none}
.btn .btn-icon{width:34px;height:34px;border:3px solid var(--green);border-right:none;background:var(--white);display:flex;align-items:center;justify-content:center}
.btn .btn-label{background:var(--green);height:26px;padding:0 16px;display:flex;align-items:center}

/* top bar + header */
.topbar{top:0;left:0;width:1200px;height:30px;background:var(--green)}
.topbar .phone{right:128px;top:5px;color:var(--white);font-size:15px;display:flex;align-items:center;gap:8px}
.topbar .login{right:40px;top:4px;background:var(--green-dark);color:var(--white);font-size:13px;padding:3px 12px;border:1px solid #9fd46f}
.header{top:30px;left:0;width:1200px;height:83px;background:var(--white)}
.brand{left:162px;top:14px;display:flex;align-items:center;gap:12px;font-weight:700;font-size:30px;color:var(--navy)}
.brand .mark{width:48px;height:48px;border:3px solid var(--green)}
.nav{right:150px;top:30px;display:flex;gap:48px;font-size:15px;color:var(--ink)}
.nav .active{border-bottom:2px solid var(--green);padding-bottom:4px}

/* hero */
.hero{top:113px;left:0;width:1200px;height:511px;background:radial-gradient(ellipse at 62% 45%,#6f8566 0%,#3f5138 38%,#26302a 75%,#1b211e 100%)}
.hero h1{position:absolute;top:150px;left:0;width:1200px;text-align:center;font-family:"Oswald",sans-serif;font-weight:400;font-size:64px;color:var(--white)}
.hero p{position:absolute;top:240px;left:0;width:1200px;text-align:center;font-size:26px;color:var(--white)}
.hero .btn{position:absolute;top:290px;left:525px}
.hero .dots{position:absolute;top:462px;left:544px;display:flex;gap:16px}
.hero .dots i{width:16px;height:16px;border:2px solid var(--white);display:block}
.hero .dots i.on{background:var(--white)}

/* partner strip */
.partners{top:630px;left:0;width:1200px;height:102px;background:var(--light)}
.partners .arrow{top:30px;width:30px;height:40px}
.partners .badge{top:25px;width:128px;height:52px;background:var(--white);border:1px solid var(--line)}

/* about */
.about h2{top:792px}
.about p{top:856px;left:150px;width:900px;font-size:14px;line-height:24px;text-align:center;position:absolute}
.about .btn{position:absolute;top:990px;left:527px}

/* features */
.features-band{top:1120px;left:0;width:1200px;height:361px;background:var(--navy)}
.feature-box{top:1100px;width:170px;height:150px;border:12px solid var(--white);background:var(--white)}
.feature-box .frame{position:absolute;inset:0;border:12px solid var(--navy);background:var(--white)}
.feature-icon{position:absolute;left:49px;top:39px;width:48px;height:48px}
.feature-text{top:1278px;width:270px;color:var(--white);font-size:14px;line-height:24px;text-align:center}

/* membership */
.membership{top:1481px;left:0;width:1200px;height:718px;background:var(--light)}
.plan{top:1654px;width:278px;height:451px;background:var(--white);box-shadow:0 2px 6px rgba(0,0,0,.08)}
.plan .plan-head{height:162px;background:var(--green);color:var(--white);font-family:"Oswald",sans-serif;font-size:27px;line-height:32px;text-align:center;padding-top:30px}
.plan .price{position:absolute;top:119px;left:81px;width:116px;height:114px;background:var(--navy);border:4px solid var(--white);outline:1px solid var(--navy);color:var(--white);display:flex;align-items:center;justify-content:center;font-family:"Oswald",sans-serif;font-size:42px}
.plan .price sup{font-size:15px;align-self:flex-start;margin-top:26px}
.plan .price small{font-size:10px;font-family:"Mulish",sans-serif;margin-top:18px;margin-left:2px}
.plan ul{position:absolute;top:250px;left:46px;width:186px;list-style:none;text-align:center;font-size:15px}
.plan li{padding:9px 0;border-bottom:1px solid var(--line)}
.plan .btn{position:absolute;top:380px;left:46px}

/* chart */
.growth h2{top:2258px}
.growth p{top:2332px;left:150px;width:900px;font-size:14px;line-height:24px;text-align:center;position:absolute}
.chart{top:2420px;left:160px;width:880px;height:540px}

/* testimonials */
.experts{top:3078px;left:0;width:1200px;height:369px;background:linear-gradient(110deg,#17305a 0%,#1b3a6a 45%,#12264a 100%)}
.quote{top:3248px;width:278px;height:199px;background:var(--white);border-radius:6px;box-shadow:0 6px 12px rgba(0,0,0,.18);text-align:center;padding:14px 24px}
.quote .score{font-family:"Oswald",sans-serif;font-size:34px;color:var(--green)}
.quote .body{font-size:13px;font-style:italic;line-height:19px;margin-top:6px}
.quote .who{font-size:13px;margin-top:12px}

/* blog */
.post{top:3631px;width:440px;height:227px;background:var(--light)}
.post .photo{position:absolute;left:0;top:0;width:204px;height:227px}
.post .date{position:absolute;right:0;top:-14px;width:60px;height:62px;background:var(--green);color:var(--white);text-align:center;font-size:13px;line-height:26px}
.post .date b{display:block;background:var(--navy);font-weight:400}
.post h3{position:absolute;left:222px;top:64px;width:160px;font-size:14px;font-weight:600;line-height:20px;color:var(--ink)}
.post .excerpt{position:absolute;left:222px;top:136px;width:160px;font-size:12px;font-style:italic;line-height:18px}
.post .more{position:absolute;right:16px;bottom:12px;width:20px;height:20px;border:2px solid var(--green);color:var(--green);font-size:14px;line-height:15px;text-align:center}

/* footer */
.footer{top:3938px;left:0;width:1200px;height:284px;background:var(--footer);color:var(--white)}
.footer h4{position:absolute;top:42px;font-family:"Oswald",sans-serif;font-weight:400;font-size:19px}
.footer .field{position:absolute;left:162px;width:190px;height:28px;background:#141414;border:1px solid #2e2e2e;font-size:11px;padding:6px 10px;color:#cfcfcf}
.footer .links{position:absolute;left:400px;top:86px;list-style:none;font-size:12px;line-height:23px;color:#d5d5d5}
.footer .links li::before{content:"› ";color:var(--green)}
.footer .links .active{color:var(--green)}
.footer .news-text{position:absolute;left:556px;top:84px;width:190px;font-size:12px;line-height:18px;color:#d5d5d5}
.footer .foot-brand{position:absolute;left:826px;top:136px;font-size:28px;font-weight:700;color:var(--white)}
.footer .foot-mark{position:absolute;left:890px;top:76px;width:52px;height:52px;border:3px solid #bbbbbb}
.footer .social{position:absolute;top:186px;width:26px;height:26px;border:2px solid #bbbbbb}
.footer .btn{position:absolute}
.footer .btn .btn-icon{background:var(--footer)}
.bottombar{top:4222px;left:0;width:1200px;height:33px;background:var(--navy);color:var(--white);font-size:12px;text-align:center;line-height:33px}
</style>
</head>
<body>

<div class="abs topbar">
  <div class="abs phone">
    <svg width="20" height="20" viewBox="0 0 24 24"><rect x="1" y="1" width="22" height="22" fill="none" stroke="#fff" stroke-width="2"/><path d="M8 6l2 3-1.5 1.5a8 8 0 0 0 5 5L15 14l3 2-1 2.5C11 18 6 13 5.5 7z" fill="#fff"/></svg>
    555.014.2290
  </div>
  <div class="abs login">Login</div>
</div>

<header class="abs header">
  <div class="abs brand"><span class="mark"></span>yieldcompass Plans</div>
  <nav class="abs nav">
    <span class="active">Home</span><span>About Us</span><span>Pricing</span><span>Blog</span><span>Contact Us</span>
  </nav>
</header>

<section class="abs hero" role="img" aria-label="Photo of cupped hands holding coins with a young green plant sprouting from them">
  <h1>Win More, Lose Less</h1>
  <p>Investment strategies that boost returns and limit risk.</p>
  <a class="btn"><span class="btn-icon"><svg width="16" height="16" viewBox="0 0 16 16"><path d="M2 12l4-4 3 3 5-6" fill="none" stroke="#7dc243" stroke-width="2"/></svg></span><span class="btn-label">FREE SIGN-UP</span></a>
  <div class="dots"><i></i><i class="on"></i><i></i></div>
</section>

<section class="abs partners">
  <svg class="abs arrow" style="left:90px" viewBox="0 0 30 40"><path d="M22 4L8 20l14 16" fill="none" stroke="#9aa3ad" stroke-width="2"/></svg>
  <div class="abs badge" style="left:165px"></div>
  <div class="abs badge" style="left:310px"></div>
  <div class="abs badge" style="left:455px"></div>
  <div class="abs badge" style="left:600px"></div>
  <div class="abs badge" style="left:745px"></div>
  <div class="abs badge" style="left:890px"></div>
  <svg class="abs arrow" style="left:1080px" viewBox="0 0 30 40"><path d="M8 4l14 16L8 36" fill="none" stroke="#9aa3ad" stroke-width="2"/></svg>
</section>

<section class="about">
  <h2 class="section-title">About yieldcompass <span>Plans</span></h2>
  <p>Lorem ipsum dolor sit amet, consectetuer adipiscing elit, sed diam nonummy nibh euismod tincidunt ut laoreet dolore magna aliquam erat volutpat. Ut wisi enim ad minim veniam, quis nostrud exerci tation ullamcorper suscipit lobortis nisl ut aliquip ex ea commodo consequat. Duis autem vel eum iriure dolor in hendrerit in vulputate velit esse molestie consequat, Lorem ipsum dolor sit amet, consectetuer adipiscing elit, sed diam nonummy nibh euismod tincidunt ut laoreet dolore magna aliquam erat volutpat.</p>
  <a class="btn"><span class="btn-icon"><svg width="16" height="16" viewBox="0 0 16 16"><path d="M2 12l4-4 3 3 5-6" fill="none" stroke="#7dc243" stroke-width="2"/></svg></span><span class="btn-label">Read More</span></a>
</section>

<section class="features">
  <div class="abs features-band"></div>

  <div class="abs feature-box" style="left:200px"><div class="frame"></div>
    <svg class="feature-icon" viewBox="0 0 48 48"><path d="M14 22v-7a10 10 0 0 1 20 0v7" fill="none" stroke="#7dc243" stroke-width="5"/><rect x="8" y="22" width="32" height="24" rx="3" fill="#7dc243"/></svg>
  </div>
  <div class="abs feature-box" style="left:515px"><div class="frame"></div>
    <svg class="feature-icon" viewBox="0 0 48 48"><rect x="4" y="12" width="8" height="24" rx="2" fill="#7dc243"/><rect x="36" y="12" width="8" height="24" rx="2" fill="#7dc243"/><rect x="14" y="6" width="6" height="36" rx="2" fill="#7dc243"/><rect x="28" y="6" width="6" height="36" rx="2" fill="#7dc243"/><rect x="20" y="21" width="8" height="6" fill="#7dc243"/></svg>
  </div>
  <div class="abs feature-box" style="left:830px"><div class="frame"></div>
    <svg class="feature-icon" viewBox="0 0 48 48"><rect x="5" y="9" width="38" height="35" rx="3" fill="none" stroke="#7dc243" stroke-width="4"/><rect x="5" y="9" width="38" height="9" fill="#7dc243"/><path d="M14 4v9M34 4v9" stroke="#7dc243" stroke-width="4"/><path d="M15 30l6 6 12-12" fill="none" stroke="#7dc243" stroke-width="4"/></svg>
  </div>

  <p class="abs feature-text" style="left:150px">When you can't afford to lose, our model portfolios can protect investments by reducing holdings to risky assets when the market turns down.</p>
  <p class="abs feature-text" style="left:465px">Our dynamic portfolios find the best places to invest. They adjust monthly to invest in the strongest funds.</p>
  <p class="abs feature-text" style="left:780px">You receive monthly email recommendations generated from our systematic, rules-based models.</p>
</section>

<section class="abs membership"></section>
<h2 class="section-title" style="top:1550px">Become <span>a Member</span></h2>

<article class="abs plan" style="left:163px">
  <div class="plan-head">Limited<br>Free Membership</div>
  <div class="price">Free</div>
  <ul><li>Basic Strategies</li><li>Trends Tracker</li></ul>
  <a class="btn"><span class="btn-icon"><svg width="16" height="16" viewBox="0 0 16 16"><path d="M2 12l4-4 3 3 5-6" fill="none" stroke="#7dc243" stroke-width="2"/></svg></span><span class="btn-label">Free Membership</span></a>
</article>
<article class="abs plan" style="left:461px">
  <div class="plan-head">Monthly<br>Membership</div>
  <div class="price"><sup>$</sup>19<sup>95</sup><small>Monthly</small></div>
  <ul><li>Basic Strategies</li><li>Advanced Strategies</li><li>Trends Tracker</li></ul>
  <a class="btn"><span class="btn-icon"><svg width="16" height="16" viewBox="0 0 16 16"><path d="M2 12l4-4 3 3 5-6" fill="none" stroke="#7dc243" stroke-width="2"/></svg></span><span class="btn-label">Monthly Membership</span></a>
</article>
<article class="abs plan" style="left:760px">
  <div class="plan-head">Annual<br>Membership</div>
  <div class="price"><sup>$</sup>149<sup>95</sup><small>Annual</small></div>
  <ul><li>Basic Strategies</li><li>Advanced Strategies</li><li>Trends Tracker</li></ul>
  <a class="btn"><span class="btn-icon"><svg width="16" height="16" viewBox="0 0 16 16"><path d="M2 12l4-4 3 3 5-6" fill="none" stroke="#7dc243" stroke-width="2"/></svg></span><span class="btn-label">Annual Membership</span></a>
</article>

<section class="growth">
  <h2 class="section-title">Our Growth <span>Chart</span></h2>
  <p>Lorem ipsum dolor sit amet, consectetuer adipiscing elit, sed diam nonummy nibh euismod tincidunt ut laoreet dolore magna aliquam erat volutpat. Ut wisi enim ad minim veniam, quis nostrud exerci tation ullamcorper suscipit lobortis nisl ut aliquip.</p>
  <svg class="abs chart" viewBox="0 0 1000 540" font-family="Mulish, sans-serif" font-size="16" fill="#555">
    <defs><linearGradient id="area" x1="0" y1="0" x2="0" y2="1"><stop offset="0" stop-color="#8fbfee"/><stop offset="1" stop-color="#e6f1fb"/></linearGradient></defs>
    <g stroke="#e4e7eb" stroke-width="1">
      <line x1="60" y1="20" x2="960" y2="20"/><line x1="60" y1="120" x2="960" y2="120"/><line x1="60" y1="220" x2="960" y2="220"/><line x1="60" y1="320" x2="960" y2="320"/><line x1="60" y1="420" x2="960" y2="420"/>
    </g>
    <g text-anchor="end"><text x="40" y="26">1</text><text x="40" y="126">0.9</text><text x="40" y="226">0.8</text><text x="40" y="326">0.7</text><text x="40" y="426">0.6</text></g>
    <path d="M60 240L80 260L100 300L120 320L140 360L160 380L180 300L200 220L220 260L240 230L260 280L280 320L300 260L320 200L340 240L360 290L380 270L400 220L420 250L440 280L460 240L480 190L500 230L520 260L540 240L560 290L580 310L600 280L620 300L640 270L660 280L680 250L700 230L720 170L740 70L760 100L780 140L800 90L820 120L840 160L860 110L880 60L900 100L920 150L940 170L960 180L960 420L60 420Z" fill="url(#area)"/>
    <path d="M60 240L80 260L100 300L120 320L140 360L160 380L180 300L200 220L220 260L240 230L260 280L280 320L300 260L320 200L340 240L360 290L380 270L400 220L420 250L440 280L460 240L480 190L500 230L520 260L540 240L560 290L580 310L600 280L620 300L640 270L660 280L680 250L700 230L720 170L740 70L760 100L780 140L800 90L820 120L840 160L860 110L880 60L900 100L920 150L940 170L960 180" fill="none" stroke="#6aa7e0" stroke-width="2"/>
    <g fill="#7dc243"><circle cx="60" cy="240" r="6"/><circle cx="200" cy="220" r="6"/><circle cx="320" cy="200" r="6"/><circle cx="400" cy="220" r="6"/><circle cx="480" cy="190" r="6"/><circle cx="740" cy="70" r="6"/><circle cx="800" cy="90" r="6"/><circle cx="880" cy="60" r="6"/></g>
    <line x1="60" y1="420" x2="960" y2="420" stroke="#c9ced5"/>
    <g text-anchor="middle"><text x="142" y="512">2008</text><text x="306" y="512">2010</text><text x="469" y="512">2012</text><text x="633" y="512">2014</text><text x="796" y="512">2016</text><text x="960" y="512">2018</text></g>
  </svg>
</section>

<section class="abs experts" role="img" aria-label="Dark blue photo of a hand reaching toward a rising financial arrow graphic"></section>
<h2 class="section-title" style="top:3146px;color:#fff">What The Experts <span>Are Saying</span></h2>
<blockquote class="abs quote" style="left:163px"><div class="score">10/10</div><p class="body">" Lorem ipsum dolor sit amet, consecte tuer adipiscing elit, sed diam nonu mmy nibh euismod tincidunt ut laoreet dolore magna aliquam erat volutpat. "</p><p class="who">- Consecte Tadipiscing</p></blockquote>
<blockquote class="abs quote" style="left:461px"><div class="score">9.5/10</div><p class="body">" Lorem ipsum dolor sit amet, consecte tuer adipiscing elit, sed diam nonu mmy nibh euismod tincidunt ut laoreet dolore magna aliquam erat volutpat. "</p><p class="who">- Euismod Tincidunt</p></blockquote>
<blockquote class="abs quote" style="left:760px"><div class="score">9.5/10</div><p class="body">" Lorem ipsum dolor sit amet, consecte tuer adipiscing elit, sed diam nonu mmy nibh euismod tincidunt ut laoreet dolore magna aliquam erat volutpat. "</p><p class="who">- Magna Aliquam</p></blockquote>

<section class="blog">
  <h2 class="section-title" style="top:3534px">Latest <span>Blog</span></h2>
  <article class="abs post" style="left:163px">
    <div class="photo" role="img" aria-label="Night photo of a city skyline with glowing streets" style="background:linear-gradient(160deg,#2b3f6e 0%,#6b4a5c 55%,#d88a3a 100%)"></div>
    <div class="date">10 Jan<b>2018</b></div>
    <h3>5 Single-Country ETFs that Outperformed the US in 2017</h3>
    <p class="excerpt">Last year was a big year for foreign markets for US investors.</p>
    <div class="more">+</div>
  </article>
  <article class="abs post" style="left:630px">
    <div class="photo" role="img" aria-label="Photo of a snow-capped mountain peak at sunset" style="background:linear-gradient(170deg,#e7a774 0%,#a8a9b0 45%,#4a5058 100%)"></div>
    <div class="date">10 Jan<b>2018</b></div>
    <h3>5 Single-Country ETFs that Outperformed the US in 2017</h3>
    <p class="excerpt">Last year was a big year for foreign markets for US investors.</p>
    <div class="more">+</div>
  </article>
</section>

<footer class="abs footer">
  <h4 style="left:162px">Contact Us</h4>
  <div class="field" style="top:88px">Name</div>
  <div class="field" style="top:126px">Email</div>
  <div class="field" style="top:164px">Message</div>
  <a class="btn" style="left:162px;top:214px"><span class="btn-icon"><svg width="16" height="16" viewBox="0 0 16 16"><path d="M2 12l4-4 3 3 5-6" fill="none" stroke="#7dc243" stroke-width="2"/></svg></span><span class="btn-label">Submit</span></a>

  <h4 style="left:400px">Quick Links</h4>
  <ul class="links"><li class="active">Home</li><li>About Us</li><li>Pricing</li><li>Blog</li><li>Contact Us</li></ul>

  <h4 style="left:556px">Join Our Newsletter</h4>
  <p class="news-text">Subscribe to our Newsletter to get the latest scoop right to your inbox.</p>
  <div class="field" style="left:556px;top:146px;width:180px">Enter Your Email</div>
  <a class="btn" style="left:556px;top:190px"><span class="btn-icon"><svg width="16" height="16" viewBox="0 0 16 16"><path d="M2 12l4-4 3 3 5-6" fill="none" stroke="#7dc243" stroke-width="2"/></svg></span><span class="btn-label">Subscribe</span></a>

  <div class="foot-mark"></div>
  <div class="foot-brand">yieldcompass Plans</div>
  <span class="social" style="left:870px"></span>
  <span class="social" style="left:903px"></span>
  <span class="social" style="left:936px"></span>
</footer>
<div class="abs bottombar">© 2018 Yieldcompassplans Financial Investments All Rights Reserved.</div>

</body>
</html>
```